LBFC Business cards

We are an established dental practice that is looking for new business cards to match our new logo. We are looking for something unique and sophisticated.
BRIEF: Colours are black, silver and white. Include the company name, logo (including “Larkspur Bend Family Care”) and phone number “03 9416 2857”.
Front - Include the company name, logo (including “Larkspur Bend Family Care”) and phone number “03 9416 2857”.
Back - Include the company name,  “Larkspur Bend Family Care”, phone number “03 9416 2857”. address "84C Tilbury Street, Larkspur Bend, Vic 3187", "Email reception@larkspurbendfamilycare.com.au", the Dentist Name " Dr ................................"  Your next appointment "Day, date and time(am/pm)".  3 lines for 3 appointments please, and at the bottom "IF UNABLE TO KEEP THIS APPOINTMENT 48 HOURS NOTICE IS REQUIRED."
Try and be creative and different with the design, i've added an image for inspiration

Target Market(s)
ALL in need of dental
Industry/Entity Type
Dental Clinic

```html
<!DOCTYPE html>
<html lang="en">
<head>
<meta charset="utf-8">
<title>LBFC Business Cards</title>
<link href="https://fonts.googleapis.com/css2?family=Montserrat:wght@500;600&family=Questrial&display=swap" rel="stylesheet">
<style>
  :root {
    --backdrop: #3a3a3a;
    --card: #1a1a1a;
    --white: #ffffff;
    --silver: #b9b9b9;
    --silver-dark: #8d8d8d;
    --ink: #1a1a1a;
  }
  * { margin: 0; padding: 0; box-sizing: border-box; }
  html, body { width: 1200px; height: 1059px; overflow: hidden; }
  body {
    background: var(--backdrop);
    position: relative;
    font-family: "Questrial", "Century Gothic", sans-serif;
    color: var(--white);
  }
  .card {
    position: absolute;
    background: var(--card);
    border-radius: 18px;
    overflow: hidden;
  }
  .card--front { left: 257px; top: 100px; width: 687px; height: 391px; }
  .card--back { left: 253px; top: 537px; width: 694px; height: 394px; }

  .brand-name {
    font-family: "Montserrat", sans-serif;
    font-weight: 600;
    color: var(--white);
    text-transform: uppercase;
    line-height: 1;
    white-space: nowrap;
  }
  .brand-name span { display: block; }

  .front-brand { position: absolute; left: 28px; top: 134px; }
  .front-brand .line-main { font-size: 33px; letter-spacing: 0.5px; }
  .front-brand .line-sub { font-size: 15.5px; letter-spacing: 3.2px; margin-top: 7px; }

  .front-phone {
    position: absolute; left: 28px; top: 214px;
    display: flex; align-items: center; gap: 13px;
  }
  .phone-badge {
    width: 39px; height: 39px; border-radius: 50%;
    background: var(--white);
    display: flex; align-items: center; justify-content: center;
  }
  .front-phone .number { font-family: "Montserrat", sans-serif; font-weight: 500; font-size: 31px; }

  .brand-disc {
    position: absolute; left: 417px; top: 72px;
    width: 246px; height: 246px; border-radius: 50%;
    background: linear-gradient(90deg, var(--silver-dark), #e2e2e2 35%, var(--silver) 55%, #e8e8e8 80%, var(--silver-dark));
  }

  .divider { position: absolute; left: 368px; top: 32px; width: 1px; height: 278px; background: var(--silver); }

  .dentist { position: absolute; left: 24px; top: 68px; }
  .dentist .name { font-family: "Montserrat", sans-serif; font-weight: 600; font-size: 22.5px; }
  .dentist .role { font-size: 18.5px; margin-top: 4px; }

  .address { position: absolute; left: 24px; top: 166px; font-size: 14px; line-height: 17.5px; }
  .contacts { position: absolute; left: 24px; top: 202px; list-style: none; font-size: 13.6px; }
  .contacts li { display: flex; align-items: center; gap: 5px; height: 21px; }
  .contacts svg { flex: none; }

  .back-brand-mark {
    position: absolute; left: 394px; top: 34px;
    width: 46px; height: 46px; border-radius: 50%;
    border: 2px solid var(--white);
  }
  .back-brand { position: absolute; left: 453px; top: 40px; }
  .back-brand .line-main { font-size: 20.5px; }
  .back-brand .line-sub { font-size: 9.6px; letter-spacing: 1.9px; margin-top: 4px; }

  .appointments { position: absolute; left: 381px; top: 111px; width: 291px; }
  .appointments h2 { font-weight: 400; font-size: 16px; letter-spacing: 0.2px; }
  .note-line { border-bottom: 1px dashed var(--silver); height: 1px; }
  .note-line:nth-of-type(1) { margin-top: 33px; }
  .note-line:nth-of-type(2) { margin-top: 22px; }
  .slots { list-style: none; margin-top: 28px; font-size: 13.5px; }
  .slots li { display: flex; align-items: baseline; height: 33px; }
  .slots .fill { flex: 1; border-bottom: 1px dashed var(--silver); margin: 0 4px; transform: translateY(-2px); }

  .notice-band {
    position: absolute; left: 0; top: 329px; width: 100%; height: 31px;
    background: var(--white); color: var(--ink);
    font-size: 15.5px; letter-spacing: 0.2px;
    display: flex; align-items: center; justify-content: center;
  }
</style>
</head>
<body>

<section class="card card--front" aria-label="Card front">
  <div class="brand-name front-brand">
    <span class="line-main">Larkspur Bend</span>
    <span class="line-sub">Family Care — 03 9416 2857</span>
  </div>
  <div class="front-phone">
    <div class="phone-badge">
      <svg width="20" height="20" viewBox="0 0 24 24" fill="var(--ink)"><path d="M6.6 10.8a15.1 15.1 0 0 0 6.6 6.6l2.2-2.2c.3-.3.7-.4 1-.2 1.1.4 2.3.6 3.6.6.6 0 1 .4 1 1V20c0 .6-.4 1-1 1A17 17 0 0 1 3 4c0-.6.4-1 1-1h3.5c.6 0 1 .4 1 1 0 1.3.2 2.5.6 3.6.1.3 0 .7-.2 1z"/></svg>
    </div>
    <span class="number">03 9416 2857</span>
  </div>
  <div class="brand-disc"></div>
</section>

<section class="card card--back" aria-label="Card back">
  <div class="dentist">
    <p class="name">Dr Helen Marsby</p>
    <p class="role">Dentist</p>
  </div>
  <p class="address">84C Tilbury Street,<br>Larkspur Bend, Vic 3187</p>
  <ul class="contacts">
    <li>
      <svg width="11" height="11" viewBox="0 0 24 24" fill="var(--white)"><path d="M6.6 10.8a15.1 15.1 0 0 0 6.6 6.6l2.2-2.2c.3-.3.7-.4 1-.2 1.1.4 2.3.6 3.6.6.6 0 1 .4 1 1V20c0 .6-.4 1-1 1A17 17 0 0 1 3 4c0-.6.4-1 1-1h3.5c.6 0 1 .4 1 1 0 1.3.2 2.5.6 3.6.1.3 0 .7-.2 1z"/></svg>
      03 9416 2857
    </li>
    <li>
      <svg width="11" height="9" viewBox="0 0 24 18" fill="var(--white)"><path d="M0 0h24v18H0z"/><path d="M1 1l11 9 11-9" fill="none" stroke="var(--card)" stroke-width="2"/></svg>
      reception@larkspurbendfamilycare.com.au
    </li>
    <li>
      <svg width="11" height="11" viewBox="0 0 24 24" fill="none" stroke="var(--white)" stroke-width="2.5"><circle cx="12" cy="12" r="10"/><path d="M2 12h20M12 2c3 3 3 17 0 20M12 2c-3 3-3 17 0 20"/></svg>
      larkspurbendfamilycare.com.au
    </li>
  </ul>

  <div class="divider"></div>

  <div class="back-brand-mark"></div>
  <div class="brand-name back-brand">
    <span class="line-main">Larkspur Bend</span>
    <span class="line-sub">Family Care — 03 9416 2857</span>
  </div>

  <div class="appointments">
    <h2>NEXT APPOINTMENT</h2>
    <div class="note-line"></div>
    <div class="note-line"></div>
    <ul class="slots">
      <li>Date <span class="fill"></span> At <span class="fill"></span> am/pm</li>
      <li>Date <span class="fill"></span> At <span class="fill"></span> am/pm</li>
      <li>Date <span class="fill"></span> At <span class="fill"></span> am/pm</li>
    </ul>
  </div>

  <p class="notice-band">IF UNABLE TO KEEP THIS APPOINTMENT 48 HOURS NOTICE IS REQUIRED</p>
</section>

</body>
</html>
```